Business card for a "family office" company

Please provide professional looking business card designs, incorporating the attached logo and below details. Harrowmere Holdings Pty Ltd is a family office / financial investment company. We are looking for a modern, professional and contemporary card design.

Industry/Entity Type

Finance

Contact Information for Business Card

Name: Dean Malcott
Title: Director
Company: Harrowmere Holdings Pty Ltd
Email: harrowlead@ozmailnet.com.au
Mobile: 0492 635 718
Address: 3/412 Bramwood Parade, Ellbrook WA 6075, Australia

Requirements
Must have
• All details above and the logo. logo only on back side. incorporate colours of logo
Nice to have
• up to you
Should not have
• ?

```html
<!DOCTYPE html>
<html lang="en">
<head>
<meta charset="utf-8">
<title>Harrowmere Holdings – Business Card</title>
<link rel="stylesheet" href="https://fonts.googleapis.com/css2?family=Bitter:wght@600&family=Lato:wght@400&display=swap">
<style>
  :root {
    --backdrop: #6e6e6e;
    --card-white: #ffffff;
    --navy: #1f1e5c;
    --navy-pattern: #24236a;
    --name-blue: #23309a;
    --ink: #1b1b1b;
    --rule: #9a9a9a;
  }
  * { margin: 0; padding: 0; box-sizing: border-box; }
  html, body {
    width: 1200px; height: 900px; overflow: hidden;
    background: var(--backdrop);
  }
  .stage { position: relative; width: 1200px; height: 900px; }
  .card {
    position: absolute; top: 306px;
    width: 440px; height: 271px;
    border-radius: 12px; overflow: hidden;
  }
  .card--front { left: 149px; background: var(--card-white); }
  .card--back { left: 608px; background: var(--navy); }

  .brand {
    position: absolute; left: 18px; top: 74px; width: 202px; height: 122px;
    display: flex; align-items: center; justify-content: center; gap: 10px;
    color: var(--navy);
    font-family: "Bitter", Georgia, serif; font-weight: 600;
  }
  .brand__square { width: 14px; height: 14px; background: var(--navy); flex: none; }
  .brand__name { font-size: 25px; line-height: 1.15; }

  .divider {
    position: absolute; left: 232px; top: 74px;
    width: 1px; height: 122px; background: var(--rule);
  }
  .contact {
    position: absolute; left: 248px; top: 73px;
    font-family: "Lato", Arial, sans-serif; font-size: 12px;
    color: var(--ink); line-height: 16px; white-space: nowrap;
  }
  .contact__name {
    font-family: "Bitter", Georgia, serif; font-weight: 600;
    font-size: 16px; line-height: 18px; color: var(--name-blue);
    text-transform: uppercase; letter-spacing: 0.2px;
  }
  .contact__title { margin-bottom: 14px; }
  .contact__line { display: flex; align-items: center; gap: 4px; }
  .contact__line svg { width: 11px; height: 11px; flex: none; }
  .contact__address { margin-top: 11px; }

  .back-pattern {
    position: absolute; inset: 0;
    background: linear-gradient(180deg, var(--navy-pattern), var(--navy));
  }
  .back-brand {
    position: absolute; inset: 0;
    display: flex; align-items: center; justify-content: center; gap: 12px;
    color: #ffffff;
    font-family: "Bitter", Georgia, serif; font-weight: 600; font-size: 30px;
  }
  .back-brand__square { width: 16px; height: 16px; background: #ffffff; }
</style>
</head>
<body>
<main class="stage">
  <section class="card card--front">
    <div class="brand">
      <span class="brand__square"></span>
      <span class="brand__name">Harrowmere<br>Holdings</span>
    </div>
    <div class="divider"></div>
    <div class="contact">
      <p class="contact__name">Dean Malcott</p>
      <p class="contact__title">Director</p>
      <p class="contact__line">
        <svg viewBox="0 0 24 24" aria-hidden="true"><path fill="#1f1e5c" d="M6.6 10.8a15.1 15.1 0 0 0 6.6 6.6l2.2-2.2c.3-.3.7-.4 1-.2 1.1.4 2.3.6 3.6.6.6 0 1 .4 1 1V20c0 .6-.4 1-1 1A17 17 0 0 1 3 4c0-.6.4-1 1-1h3.5c.6 0 1 .4 1 1 0 1.3.2 2.5.6 3.6.1.3 0 .7-.2 1z"/></svg>
        0492 635 718
      </p>
      <p class="contact__line">
        <svg viewBox="0 0 24 24" aria-hidden="true"><path fill="#1f1e5c" d="M2 5h20v14H2z"/><path fill="none" stroke="#fff" stroke-width="1.8" d="M2.5 5.5 12 13l9.5-7.5"/></svg>
        harrowlead@ozmailnet.com.au
      </p>
      <p class="contact__address">3/412 Bramwood Parade,<br>Ellbrook WA 6075, Australia</p>
    </div>
  </section>

  <section class="card card--back">
    <div class="back-pattern" role="img" aria-label="Faint repeating pattern of the company symbol on navy"></div>
    <div class="back-brand">
      <span class="back-brand__square"></span>
      <span>Harrowmere Holdings</span>
    </div>
  </section>
</main>
</body>
</html>
```